Business Card Design Project

Need a business card that stands my education platform as a whole but

Target Market(s)

Parents, families, expats in the middle east.

Industry/Entity Type

Education

Contact Information for Business Card

www.brightlane.ae
www.homesteadhub.ae
www.littlenestcarers.ae

+971552419736
helena@brightlane.ae

Font styles to use
Serif

Requirements
Must have
• Logo's and contact details

```html
<!DOCTYPE html>
<html lang="en">
<head>
<meta charset="utf-8">
<title>Bright Lane – Business Card</title>
<link rel="stylesheet" href="https://fonts.googleapis.com/css2?family=Nunito:wght@600;700;800&display=swap">
<style>
  :root {
    --teal: #3f89a5;
    --teal-soft: #cfe2ea;
    --orange: #f08a4b;
    --orange-soft: #fbd9c3;
    --card: #ffffff;
    --stage: #2b2b2b;
    --ghost: #eeeeee;
    --white: #ffffff;
  }
  * { box-sizing: border-box; margin: 0; padding: 0; }
  html, body { width: 1200px; height: 800px; overflow: hidden; }
  body {
    background: var(--stage);
    font-family: "Nunito", sans-serif;
    position: relative;
  }
  .card {
    position: absolute;
    top: 114px;
    width: 340px;
    height: 572px;
    background: var(--card);
    overflow: hidden;
  }
  .card--front { left: 233px; }
  .card--back { left: 627px; }

  /* front */
  .pattern {
    position: absolute;
    left: 14px;
    right: 14px;
  }
  .pattern--top {
    top: 0;
    height: 100px;
    background: linear-gradient(180deg, var(--teal) 0%, var(--teal-soft) 100%);
    border-radius: 0 0 10px 10px;
  }
  .pattern--bottom {
    bottom: 0;
    height: 92px;
    background: linear-gradient(0deg, var(--orange) 0%, var(--orange-soft) 100%);
    border-radius: 10px 10px 0 0;
  }
  .brand-name {
    position: absolute;
    top: 148px;
    left: 0;
    right: 0;
    text-align: center;
    color: var(--teal);
    font-weight: 700;
    font-size: 30px;
    letter-spacing: 2px;
  }
  .brand-art {
    position: absolute;
    top: 196px;
    left: 60px;
    width: 220px;
    height: 148px;
    border-radius: 12px;
    background: linear-gradient(90deg, var(--teal-soft) 0%, var(--teal-soft) 50%, var(--orange-soft) 50%, var(--orange-soft) 100%);
  }
  .tagline {
    position: absolute;
    top: 368px;
    left: 45px;
    width: 254px;
    height: 74px;
    border-radius: 12px;
    background: var(--teal);
    color: var(--white);
    font-weight: 600;
    font-size: 18px;
    line-height: 1.25;
    display: flex;
    align-items: center;
    justify-content: center;
    text-align: center;
  }

  /* back */
  .ghost-pattern {
    position: absolute;
    inset: 0;
    background: linear-gradient(135deg, var(--white) 0%, var(--ghost) 45%, var(--white) 100%);
  }
  .pill {
    position: absolute;
    left: 0;
    display: flex;
    align-items: center;
    color: var(--white);
    font-weight: 700;
  }
  .pill--web {
    height: 40px;
    padding-left: 16px;
    background: var(--orange);
    border-radius: 0 12px 12px 0;
    font-size: 18px;
  }
  .pill--web-1 { top: 52px; width: 224px; }
  .pill--web-2 { top: 115px; width: 236px; }
  .pill--web-3 { top: 176px; width: 300px; }
  .phone-box {
    position: absolute;
    top: 292px;
    left: 78px;
    right: 0;
    height: 82px;
    background: var(--teal);
    border-radius: 14px 0 0 14px;
    color: var(--white);
    text-align: center;
    font-weight: 800;
    font-size: 26px;
  }
  .phone-icon {
    display: block;
    margin: 6px auto 2px;
    width: 30px;
    height: 30px;
  }
  .pill--mail {
    top: 451px;
    width: 286px;
    height: 70px;
    padding-left: 20px;
    background: var(--orange);
    border-radius: 0 22px 22px 0;
    font-size: 20px;
    font-weight: 600;
  }
</style>
</head>
<body>
  <section class="card card--front">
    <div class="pattern pattern--top" role="img" aria-label="Cluster of teal rounded-square ornaments"></div>
    <h1 class="brand-name">Bright Lane</h1>
    <div class="brand-art" role="img" aria-label="Brand illustration area in teal and orange"></div>
    <p class="tagline">Accelerated Learning<br>Centre</p>
    <div class="pattern pattern--bottom" role="img" aria-label="Cluster of orange rounded-square ornaments"></div>
  </section>

  <section class="card card--back">
    <div class="ghost-pattern" role="img" aria-label="Faint grey rounded-square background pattern"></div>
    <p class="pill pill--web pill--web-1">www.brightlane.ae</p>
    <p class="pill pill--web pill--web-2">www.homesteadhub.ae</p>
    <p class="pill pill--web pill--web-3">www.littlenestcarers.ae</p>
    <div class="phone-box">
      <svg class="phone-icon" viewBox="0 0 30 30" aria-hidden="true">
        <circle cx="15" cy="15" r="15" fill="#ffffff"/>
        <path d="M10.5 7.5c.6-.4 1.3-.3 1.7.3l1.7 2.6c.4.6.3 1.3-.2 1.7l-1.1.9c.8 1.9 2.3 3.4 4.2 4.3l.9-1.1c.4-.5 1.1-.6 1.7-.2l2.6 1.7c.6.4.7 1.2.3 1.7l-1.1 1.5c-.6.8-1.6 1.1-2.6.8-4.4-1.4-7.9-4.9-9.3-9.3-.3-1 0-2 .8-2.6z" fill="var(--teal)"/>
      </svg>
      +971552419736
    </div>
    <p class="pill pill--mail">helena@brightlane.ae</p>
  </section>
</body>
</html>
```